Business Card Design

We are a design build firm specializing in the construction and design of kitchens. We are a "green" company, hence the logo. Here are some IDEAS we came up with. I am asking to use this for every person in our firm, so I will need to be able to edit the text. On the back, I am thinking of a very simple design... maybe carry over the white band around the edge. Maybe a simple saying on the back "Renovating homes from Concept to Completion".

Please see our current website for our style and design info
www.cabinetrefitvalley.com (going to be forwarded to maplehearthllc.com)

Industry/Entity Type

Construction

Contact Information for Business Card

Maple Hearth Design & Construction
Dana Wickford - Chief Designer
418 Birchwood Lane
Alderbrook, CT 06190
203.555.0172 C
203.555.0149 O
www.maplehearthllc.com
mhcabinets@mailbox.example

```html
<!DOCTYPE html>
<html lang="en">
<head>
<meta charset="utf-8">
<title>Maple Hearth Design &amp; Construction – Business Card</title>
<link rel="stylesheet" href="https://fonts.googleapis.com/css2?family=Didact+Gothic&family=Montserrat:wght@600;700&display=swap">
<style>
  :root {
    --backdrop: #2e2e2e;
    --card-white: #ffffff;
    --ink: #1c2a20;
    --green-light: #8dc03f;
    --green-mid: #4f9a3a;
    --green-dark: #17672f;
    --rule-grey: #cfcfcf;
    --label-grey: #bdbdbd;
  }
  * { margin: 0; padding: 0; box-sizing: border-box; }
  html, body { width: 1200px; height: 1000px; overflow: hidden; }
  body { background: var(--backdrop); position: relative; font-family: "Didact Gothic", sans-serif; }

  .card {
    position: absolute; top: 117px; width: 423px; height: 723px;
    background: var(--card-white); overflow: hidden;
  }
  .card--front { left: 121px; }
  .card--back { left: 677px; }

  .side-label {
    position: absolute; top: 893px; width: 423px; text-align: center;
    color: var(--label-grey); font-size: 20px; font-family: "Didact Gothic", sans-serif;
  }
  .side-label--front { left: 121px; }
  .side-label--back { left: 677px; }

  /* brand block */
  .brand { position: absolute; left: 0; width: 100%; text-align: center; color: var(--ink); }
  .brand__dot { display: block; margin: 0 auto 14px; width: 38px; height: 38px; border-radius: 50%; background: var(--ink); }
  .brand__name { font-family: "Montserrat", sans-serif; font-weight: 600; font-size: 38px; letter-spacing: -0.5px; line-height: 1; }
  .brand__rule { width: 338px; height: 1px; background: #555; margin: 12px auto 8px; }
  .brand__tagline { font-family: "Montserrat", sans-serif; font-weight: 600; font-size: 18.5px; letter-spacing: 2px; line-height: 1; }

  .card--front .brand { top: 86px; }

  /* green band */
  .band { position: absolute; left: 0; width: 100%; }
  .band--front { top: 238px; height: 450px; background: linear-gradient(180deg, var(--green-light) 0%, var(--green-mid) 55%, var(--green-dark) 100%); }
  .band-edge { position: absolute; left: 0; width: 100%; height: 6px; background: var(--rule-grey); }
  .band-edge--front { top: 688px; }

  .person { position: absolute; top: 320px; left: 0; width: 100%; text-align: center; color: #fff; }
  .person__name { font-family: "Montserrat", sans-serif; font-weight: 600; font-size: 24px; letter-spacing: 0.5px; }
  .person__company { font-size: 18px; margin-top: 6px; }

  .contact { position: absolute; left: 84px; color: #fff; font-size: 20px; display: flex; align-items: center; }
  .contact__icon { width: 22px; height: 22px; margin-right: 8px; fill: #fff; flex: none; }
  .contact__lines { border-left: 2px solid #fff; padding-left: 9px; line-height: 1.45; }
  .contact--phone { top: 398px; }
  .contact--phone .contact__lines { line-height: 1.6; }
  .contact--email { top: 484px; }
  .contact--email .contact__lines { font-size: 18px; }
  .contact--web { top: 523px; }
  .contact--address { top: 580px; }
  .contact--address .contact__lines { line-height: 1.3; }

  /* back */
  .band-edge--back { top: 213px; }
  .band--back { top: 219px; height: 202px; background: linear-gradient(180deg, var(--green-light) 0%, var(--green-mid) 45%, var(--green-dark) 100%); }
  .slogan { position: absolute; top: 256px; left: 0; width: 100%; text-align: center; color: #fff; }
  .slogan__lead { font-size: 20px; letter-spacing: 1px; }
  .slogan__main { font-family: "Montserrat", sans-serif; font-weight: 700; font-size: 25px; letter-spacing: 0.3px; margin-top: 2px; }
  .back-dot { position: absolute; top: 360px; left: 192px; width: 38px; height: 38px; border-radius: 50%; background: #fff; }
  .card--back .brand { top: 440px; }
</style>
</head>
<body>

  <section class="card card--front" aria-label="Business card front">
    <div class="brand">
      <span class="brand__dot"></span>
      <div class="brand__name">MAPLE HEARTH</div>
      <div class="brand__rule"></div>
      <div class="brand__tagline">DESIGN &amp; CONSTRUCTION</div>
    </div>

    <div class="band band--front"></div>
    <div class="band-edge band-edge--front"></div>

    <div class="person">
      <div class="person__name">DANA WICKFORD</div>
      <div class="person__company">Maple Hearth Design &amp; Construction</div>
    </div>

    <div class="contact contact--phone">
      <svg class="contact__icon" viewBox="0 0 24 24" aria-hidden="true"><path d="M7 1h10a2 2 0 0 1 2 2v18a2 2 0 0 1-2 2H7a2 2 0 0 1-2-2V3a2 2 0 0 1 2-2zm0 3v14h10V4zm5 15.5a1.2 1.2 0 1 0 0 2.4 1.2 1.2 0 0 0 0-2.4z"/></svg>
      <div class="contact__lines">203.555.0172<br>203.555.0149</div>
    </div>

    <div class="contact contact--email">
      <svg class="contact__icon" viewBox="0 0 24 24" aria-hidden="true"><path d="M2 5h20v14H2zm2 2v.4l8 5.6 8-5.6V7zm0 2.8V17h16V9.8l-8 5.6z"/></svg>
      <div class="contact__lines">mhcabinets@mailbox.example</div>
    </div>

    <div class="contact contact--web">
      <svg class="contact__icon" viewBox="0 0 24 24" aria-hidden="true"><path d="M12 2a10 10 0 1 0 0 20 10 10 0 0 0 0-20zm0 2c.9 0 2.3 2 2.8 5H9.2C9.7 6 11.1 4 12 4zM4.3 11h3a17 17 0 0 0 0 2h-3a8 8 0 0 1 0-2zm4.8 0h5.8a15 15 0 0 1 0 2H9.1a15 15 0 0 1 0-2zm7.6 0h3a8 8 0 0 1 0 2h-3a17 17 0 0 0 0-2zM9.2 15h5.6c-.5 3-1.9 5-2.8 5s-2.3-2-2.8-5z"/></svg>
      <div class="contact__lines">www.maplehearthllc.com</div>
    </div>

    <div class="contact contact--address">
      <svg class="contact__icon" viewBox="0 0 24 24" aria-hidden="true"><path d="M12 1a7 7 0 0 0-7 7c0 5.2 7 15 7 15s7-9.8 7-15a7 7 0 0 0-7-7zm0 9.5A2.5 2.5 0 1 1 12 5.5a2.5 2.5 0 0 1 0 5z"/></svg>
      <div class="contact__lines">418 Birchwood Lane<br>Alderbrook, CT 06190</div>
    </div>
  </section>

  <section class="card card--back" aria-label="Business card back">
    <div class="band-edge band-edge--back"></div>
    <div class="band band--back"></div>
    <div class="slogan">
      <div class="slogan__lead">RENOVATING HOMES FROM</div>
      <div class="slogan__main">CONCEPT TO COMPLETION</div>
    </div>
    <span class="back-dot"></span>
    <div class="brand">
      <div class="brand__name">MAPLE HEARTH</div>
      <div class="brand__rule"></div>
      <div class="brand__tagline">DESIGN &amp; CONSTRUCTION</div>
    </div>
  </section>

  <div class="side-label side-label--front">Front</div>
  <div class="side-label side-label--back">Back</div>

</body>
</html>
```